Kelvor Plant Services

We are a heavy diesel mechanical business with additional air con certificates, remapping engine rebuilt

Contact Information for Business Card

Company Name, Director Name, Managing Director, Contact details, email and website

Font styles to use
Serif
Script

```html
<!DOCTYPE html>
<html lang="en">
<head>
<meta charset="utf-8">
<title>Kelvor Plant Services – Business Card</title>
<link rel="stylesheet" href="https://fonts.googleapis.com/css2?family=Libre+Baskerville:wght@400;700&family=Great+Vibes&display=swap">
<style>
  :root {
    --backdrop: #5f6366;
    --card: #ffffff;
    --navy: #2b2a7a;
    --ink: #111111;
    --muted: #333333;
    --crescent: #0d0d0d;
  }
  * { margin: 0; padding: 0; box-sizing: border-box; }
  html, body { width: 1200px; height: 780px; overflow: hidden; }
  body {
    background: var(--backdrop);
    font-family: "Libre Baskerville", Georgia, serif;
    position: relative;
  }
  .card {
    position: absolute;
    width: 540px;
    height: 309px;
    background: var(--card);
    border-radius: 26px;
    overflow: hidden;
    box-shadow: 0 10px 24px rgba(0,0,0,.35);
  }
  .card--back { left: 60px; top: 70px; }
  .card--front { left: 600px; top: 400px; }

  .brand {
    display: flex;
    align-items: center;
    gap: 10px;
    color: var(--navy);
    font-family: "Libre Baskerville", Georgia, serif;
    font-weight: 700;
    white-space: nowrap;
  }
  .brand__dot {
    width: 22px; height: 22px;
    border-radius: 50%;
    background: var(--navy);
    flex: none;
  }
  .card--back .brand {
    position: absolute;
    left: 44px; top: 192px;
    font-size: 28px;
  }
  .card--front .brand {
    position: absolute;
    left: 34px; top: 38px;
    font-size: 18px;
  }
  .card--front .brand__dot { width: 16px; height: 16px; }

  .photo { position: absolute; right: 0; top: 0; width: 540px; height: 309px; }

  .person {
    position: absolute;
    left: 30px; top: 112px;
    padding-left: 16px;
    border-left: 12px solid var(--navy);
  }
  .person__name { font-size: 19px; color: var(--navy); letter-spacing: .5px; line-height: 24px; }
  .person__name b { color: var(--ink); font-weight: 700; }
  .person__title {
    font-family: "Great Vibes", cursive;
    font-size: 21px; line-height: 22px;
    color: var(--ink);
  }

  .address {
    position: absolute;
    left: 58px; top: 172px;
    font-size: 13px; line-height: 17px; color: var(--muted);
  }
  .contacts {
    position: absolute;
    left: 44px; top: 224px;
    list-style: none;
    font-size: 13px; line-height: 19px; color: var(--ink);
  }
  .contacts li { display: flex; align-items: center; gap: 7px; white-space: nowrap; }
  .contacts svg { width: 12px; height: 12px; flex: none; }
</style>
</head>
<body>

<section class="card card--back" aria-label="Card back">
  <div class="brand"><span class="brand__dot"></span>Kelvor Plant Services</div>
</section>

<section class="card card--front" aria-label="Card front">
  <svg class="photo" viewBox="0 0 540 309">
    <defs>
      <linearGradient id="workshopTone" x1="0" y1="0" x2="1" y2="1">
        <stop offset="0" stop-color="#6e5a3a"/>
        <stop offset=".45" stop-color="#b89a3c"/>
        <stop offset="1" stop-color="#8a8a84"/>
      </linearGradient>
    </defs>
    <circle cx="600" cy="110" r="245" fill="var(--crescent)"/>
    <circle cx="622" cy="100" r="245" fill="url(#workshopTone)" role="img" aria-label="Photo of yellow heavy machinery being serviced inside a workshop"/>
  </svg>

  <div class="brand"><span class="brand__dot"></span>Kelvor Plant Services</div>

  <div class="person">
    <p class="person__name">MARCUS <b>HALE</b></p>
    <p class="person__title">Managing Director</p>
  </div>

  <p class="address">48 Orchard Row<br>Dalebrook, TN 37410</p>

  <ul class="contacts">
    <li>
      <svg viewBox="0 0 12 12"><path d="M2 1h2.5l1 3-1.5 1a6 6 0 0 0 3 3l1-1.5 3 1V11A9 9 0 0 1 1 2z" fill="var(--navy)"/></svg>
      (555) 014-2290
    </li>
    <li>
      <svg viewBox="0 0 12 12"><rect x="0.5" y="2" width="11" height="8" fill="var(--navy)"/><path d="M1 2.5l5 4 5-4" stroke="#fff" fill="none"/></svg>
      kelvorplant@mailbox.com
    </li>
    <li>
      <svg viewBox="0 0 12 12"><circle cx="6" cy="6" r="5.5" fill="var(--navy)"/><path d="M.5 6h11M6 .5c-3 3-3 8 0 11M6 .5c3 3 3 8 0 11" stroke="#fff" stroke-width=".8" fill="none"/></svg>
      www.kelvorplant.com
    </li>
  </ul>
</section>

</body>
</html>
```